Visitenkarten-Design für Garten- und Landschaftspflege
Tamuga Vent setzte meine Vorstellungen absolut super um ich kann Ihn nur weiter empfehlen. vielen dank
Zielgruppe
Baumpflege, Baumfällung, Garten und Landschaftspflege meine zielgruppe sind Privatpersonen im alter von 20-100Jahren
Aufgabenstellung
Sehr geehrte Damen und Herren, die visitenkarte sollte die angaben so enthalten wie sie auf der von mir gestallteten Visitenkarten sind ( meine ist kein maß der Dinge). Ich habe mein Logo leider nur als 3.jpg Datei. Das Logo darf im Design erändert werden aber bitte nur Feinheiten ansonsten stehen ihnen alle türen offen um kreativ zu sein.
mit freundlichen Grüßen Holger Banzow

```html
<!DOCTYPE html>
<html lang="de">
<head>
<meta charset="utf-8">
<title>Visitenkarte Baumpflege Banzow</title>
<link rel="stylesheet" href="https://fonts.googleapis.com/css2?family=Fira+Sans:wght@300;400;600&display=swap">
<style>
  :root {
    --sheet: #dcdcdc;
    --paper: #ffffff;
    --forest: #1b6348;
    --lime: #a8c43a;
    --dash: #d6d62c;
    --fence: #2f7a5a;
  }
  * { margin: 0; padding: 0; box-sizing: border-box; }
  html, body { width: 1200px; height: 2437px; overflow: hidden; }
  body {
    background: var(--sheet);
    font-family: "Fira Sans", sans-serif;
    position: relative;
  }
  .card {
    position: absolute;
    background: var(--paper);
    border: 1px solid #333;
    overflow: hidden;
    box-shadow: 12px 16px 18px rgba(0,0,0,0.28);
  }
  .card--front { left: 136px; top: 119px; width: 955px; height: 617px; }
  .card--back  { left: 136px; top: 874px; width: 961px; height: 620px; }
  .ground { position: absolute; left: 0; width: 100%; }
  .card--front .ground { top: 280px; height: 340px; }
  .card--back .ground { top: 130px; height: 500px; }
  .artwork { position: absolute; }
  .artwork--tree { left: 142px; top: 15px; width: 387px; height: 275px; background: var(--forest); border-radius: 160px 160px 0 0; }
  .artwork--fence-left { left: 24px; top: 228px; width: 180px; height: 62px; background: var(--fence); opacity: .55; }
  .artwork--fence-right { left: 536px; top: 222px; width: 200px; height: 66px; background: var(--fence); opacity: .55; }
  .artwork--tree-small { left: 660px; top: 15px; width: 180px; height: 125px; background: var(--forest); border-radius: 80px 80px 0 0; }
  .company {
    position: absolute; left: 47px; top: 320px;
    font-weight: 400; font-size: 78px; letter-spacing: 3px;
    color: var(--lime); line-height: 1; white-space: nowrap;
  }
  .contact { position: absolute; left: 49px; top: 432px; font-size: 34px; line-height: 47px; color: #fff; white-space: nowrap; }
  .contact .role { color: var(--lime); font-weight: 600; }
  .contact .sep { color: var(--lime); }
  .services-title {
    position: absolute; left: 65px; top: 82px;
    font-weight: 600; font-size: 60px; color: var(--lime); line-height: 1;
  }
  .services { position: absolute; left: 0; top: 208px; list-style: none; }
  .services li {
    position: relative; padding-left: 65px;
    font-size: 36px; font-weight: 400; line-height: 51.5px; color: #fff; white-space: nowrap;
  }
  .services li::before {
    content: ""; position: absolute; left: 0; top: 24px;
    width: 37px; height: 6px; background: var(--dash);
  }
</style>
</head>
<body>
  <section class="card card--front">
    <svg class="ground" viewBox="0 0 955 340" preserveAspectRatio="none" aria-hidden="true">
      <path d="M0 10 Q240 0 480 6 T955 0 V340 H0 Z" fill="var(--forest)"/>
    </svg>
    <div class="artwork artwork--fence-left" role="img" aria-label="Holzzaun, Illustration"></div>
    <div class="artwork artwork--fence-right" role="img" aria-label="Holzzaun, Illustration"></div>
    <div class="artwork artwork--tree" role="img" aria-label="Baum-Silhouette, Illustration"></div>
    <h1 class="company">BAUMPFLEGE BANZOW</h1>
    <div class="contact">
      <p class="role">Holger Banzow • Fachagrarwirt Baumpflege &amp; -sanierung</p>
      <p>Lindenweg 4 <span class="sep">•</span> 85599 Ahornfeld <span class="sep">•</span> Tel. 0172 555 01 23</p>
      <p>kontakt@baumpflege-banzow.de <span class="sep">•</span> baumpflege-banzow.de</p>
    </div>
  </section>

  <section class="card card--back">
    <svg class="ground" viewBox="0 0 961 500" preserveAspectRatio="none" aria-hidden="true">
      <path d="M0 8 Q300 0 600 4 T961 2 V500 H0 Z" fill="var(--forest)"/>
    </svg>
    <div class="artwork artwork--tree-small" role="img" aria-label="Kleine Baum-Silhouette, Illustration"></div>
    <h2 class="services-title">Unsere Leistungen</h2>
    <ul class="services">
      <li>Neu-Pflanzungen</li>
      <li>Herstellen der Verkehrssicherheit von Bäumen</li>
      <li>Kronenrückschnitt (Einkürzung und Kronenpflege)</li>
      <li>Prüfen von Bäumen auf Standsicherheit</li>
      <li>Fällen von Bäumen</li>
      <li>Fräsen von Wurzelstöcken</li>
      <li>Anbau und Fertigung von Gartenhäusern nach Maß</li>
    </ul>
  </section>
</body>
</html>
```